Brimlock Assurance Branding Revamp

We are a consulting company, looking for a way to display and promote our brand. We have 2 sides to the business- Brimlock (financial) and Assurance (cyber security). The financial side products relate to business necessities: card processing, website design/hosting/maintenance, VoIP phone systems. The cyber security side promotes a bundled package of 4 solutions: network vulnerability scan, dark web scan, anti-ransomeware/malware software, and image-level backups. We want people to understand that partnering with Brimlock Assurance gives them “Elevated Peace of Mind” (tagline). Current badge and logos uploaded.

Target Market(s)

Small businesses

Contact Information for Business Card

Carla Whitfield, Vice President, carla@brimlockassurance.example, 555-384-9106, www.brimlockassurance.example

Requirements
Nice to have
• I do prefer the darker background for front and back

```html
<!DOCTYPE html>
<html lang="en">
<head>
<meta charset="utf-8">
<title>Brimlock Assurance – Business Card</title>
<link rel="stylesheet" href="https://fonts.googleapis.com/css2?family=Roboto:wght@500&family=Open+Sans:wght@400;600&display=swap">
<style>
  :root {
    --backdrop: #cfcdce;
    --card: #262626;
    --card-shade: #1f1f1f;
    --band-dark: #161616;
    --brand-red: #a3141c;
    --ink-light: #ececec;
    --icon-grey: #7a7a7a;
  }
  * { box-sizing: border-box; margin: 0; padding: 0; }
  html, body { width: 1200px; height: 800px; overflow: hidden; }
  body {
    background: var(--backdrop);
    font-family: "Open Sans", sans-serif;
    display: flex;
    align-items: center;
    justify-content: center;
    gap: 40px;
  }
  .card {
    position: relative;
    width: 540px;
    height: 310px;
    background: var(--card);
    overflow: hidden;
    box-shadow: 0 6px 18px rgba(0,0,0,.25);
  }

  /* Front: tagline */
  .card-front .half-shade {
    position: absolute; top: 0; right: 0; width: 50%; height: 100%;
    background: linear-gradient(90deg, var(--card-shade) 0, var(--card) 30px);
  }
  .tagline {
    position: absolute; top: 136px; left: 0; width: 100%;
    display: flex; font-family: "Roboto", sans-serif; font-weight: 500;
    font-size: 22px; letter-spacing: 1px; text-transform: uppercase;
  }
  .tagline-lead {
    margin-left: 76px; width: 194px; padding: 4px 12px;
    background: var(--brand-red); color: var(--ink-light);
  }
  .tagline-rest {
    padding: 4px 14px; background: var(--band-dark); color: var(--brand-red);
  }

  /* Back: contact */
  .brand-lockup {
    position: absolute; left: 40px; top: 112px; width: 200px;
    display: flex; align-items: center; gap: 12px;
  }
  .brand-square { width: 22px; height: 22px; background: var(--brand-red); flex: none; }
  .brand-name {
    font-family: "Open Sans", sans-serif; font-weight: 600; font-size: 20px;
    line-height: 1.2; color: var(--brand-red);
  }
  .contact-panel {
    position: absolute; left: 256px; top: 0; width: 284px; height: 100%;
    background: linear-gradient(90deg, var(--card-shade) 0, var(--card) 24px);
  }
  .person { position: absolute; left: 20px; top: 40px; }
  .person-name {
    font-family: "Roboto", sans-serif; font-weight: 500; font-size: 22px;
    letter-spacing: 2px; color: var(--ink-light); text-transform: uppercase;
  }
  .person-title {
    font-size: 10px; font-weight: 600; letter-spacing: 1px;
    color: var(--brand-red); text-transform: uppercase;
  }
  .contact-list { position: absolute; left: 0; top: 112px; list-style: none; }
  .contact-item { display: flex; align-items: center; height: 40px; }
  .contact-icon {
    width: 40px; height: 40px; flex: none; display: flex; align-items: center; justify-content: center;
  }
  .contact-item.phone .contact-icon { background: var(--brand-red); }
  .contact-item.address .contact-icon { background: var(--band-dark); }
  .contact-item.mail .contact-icon { background: var(--icon-grey); }
  .contact-text {
    padding-left: 12px; font-size: 12px; line-height: 1.25; color: var(--ink-light);
  }
</style>
</head>
<body>

  <section class="card card-front" aria-label="Card front">
    <div class="half-shade"></div>
    <p class="tagline">
      <span class="tagline-lead">Elevated</span>
      <span class="tagline-rest">Peace of Mind</span>
    </p>
  </section>

  <section class="card card-back" aria-label="Card back">
    <div class="brand-lockup">
      <span class="brand-square"></span>
      <span class="brand-name">Brimlock Assurance</span>
    </div>
    <div class="contact-panel">
      <div class="person">
        <p class="person-name">Carla Whitfield</p>
        <p class="person-title">Vice President</p>
      </div>
      <ul class="contact-list">
        <li class="contact-item phone">
          <span class="contact-icon">
            <svg width="16" height="16" viewBox="0 0 24 24" fill="#ececec"><path d="M6.6 10.8a15 15 0 0 0 6.6 6.6l2.2-2.2a1 1 0 0 1 1-.25 11.4 11.4 0 0 0 3.6.57 1 1 0 0 1 1 1V20a1 1 0 0 1-1 1A17 17 0 0 1 3 4a1 1 0 0 1 1-1h3.5a1 1 0 0 1 1 1c0 1.25.2 2.45.57 3.6a1 1 0 0 1-.25 1z"/></svg>
          </span>
          <span class="contact-text">555-384-9106</span>
        </li>
        <li class="contact-item address">
          <span class="contact-icon">
            <svg width="14" height="18" viewBox="0 0 24 30" fill="#ececec"><path d="M12 0a10 10 0 0 0-10 10c0 7.5 10 20 10 20s10-12.5 10-20A10 10 0 0 0 12 0zm0 14a4 4 0 1 1 0-8 4 4 0 0 1 0 8z"/></svg>
          </span>
          <span class="contact-text">88 Harbor Lane<br>Suite 210, Eastfield</span>
        </li>
        <li class="contact-item mail">
          <span class="contact-icon">
            <svg width="18" height="13" viewBox="0 0 24 17"><path d="M0 0h24v17H0z" fill="#ececec"/><path d="M0 0l12 9 12-9" fill="none" stroke="#7a7a7a" stroke-width="1.6"/></svg>
          </span>
          <span class="contact-text">carla@brimlockassurance.example<br>www.brimlockassurance.example</span>
        </li>
      </ul>
    </div>
  </section>

</body>
</html>
```